Magazine Design 6 page front and back

Would like the frame work of a design template for a 12page magazine. Looking to be able to change out the images and edit myself down the road as I complete new projects.

I would like a re-design of the attached magazine to get an entire different feel. I would like more elegant. I have attached a KVR flyer just for the colors not for the layout, I attached my business card design. I attached the flyer magazine that I made just for the informational content.

This magazine is to display my experience and expertise in the business along with customer testimonials.

Will this design be a design template that I can change out the images or wording on? As I do more and more design I would like to keep updating it with new content.

I have quite a few images that I can upload but I'm not sure of the process do you create the template and them start putting in the photos?

Target Market(s)

High end Spas, Country Club, Private facilities

Industry/Entity Type

Fitness Equipment sales and Design

Colors
0054AA
0677BA
7BADD7
CADEEF
E8F1F8

Requirements
Must have
• Elegant high end feel. I would like the small logo implemented somewhere like how it is on the back of my business card.

```html
<!DOCTYPE html>
<html lang="en">
<head>
<meta charset="utf-8">
<title>Peak By Form – Statement of Qualification</title>
<link href="https://fonts.googleapis.com/css2?family=Montserrat:wght@300;400;600;700;800&display=swap" rel="stylesheet">
<style>
:root{
  --stage:#f59d00;
  --paper:#ffffff;
  --ink:#1f1f22;
  --muted:#6a6e75;
  --blue:#3d6fcf;
  --cyan:#0db3d6;
  --rule:#d9dce1;
  --bar:#e4e6e9;
}
*{margin:0;padding:0;box-sizing:border-box}
html,body{width:1200px;height:4038px;overflow:hidden}
body{background:var(--stage);font-family:"Montserrat",sans-serif;color:var(--ink);position:relative}
.page{position:absolute;background:var(--paper);box-shadow:0 18px 40px rgba(120,60,0,.35);overflow:hidden}
.abs{position:absolute}
.photo{position:absolute}
.ph-sky{background:linear-gradient(180deg,#5f86b3 0%,#9fb4c9 35%,#b68f6c 55%,#4a3a32 75%,#2f64c8 100%)}
.ph-sky-sm{background:linear-gradient(180deg,#7d9bc1 0%,#b7a592 45%,#6a4d3f 70%,#3a3330 100%)}
.ph-gym{background:linear-gradient(180deg,#e6e6e6 0%,#c9c9c9 45%,#6d6f73 70%,#b4b4b4 100%)}
.ph-gym-dark{background:linear-gradient(180deg,#2a2b2e 0%,#8a8c90 40%,#b8aa9a 70%,#6e5a4a 100%)}
.ph-gym-red{background:linear-gradient(180deg,#3a3b3f 0%,#9c9ea2 45%,#7d7f83 70%,#c4323e 100%)}
.ph-portrait{background:radial-gradient(circle at 50% 45%,#7b5a48 0%,#3a2a22 35%,#0c0c0c 70%)}
.brand{font-weight:800;font-size:11px;letter-spacing:.04em;color:var(--ink);white-space:nowrap}
.brand-mark{font-weight:800;color:var(--ink);display:flex;align-items:center;gap:8px;white-space:nowrap}
.brand-mark i{display:block;width:14px;height:14px;background:var(--blue)}
.sq{position:absolute;width:27px;height:27px}
.sq.blue{background:var(--blue)} .sq.cyan{background:var(--cyan)}
.vert{position:absolute;writing-mode:vertical-rl;transform:rotate(180deg);font-size:14.5px;line-height:1.1;color:#4a4d52;font-weight:300;white-space:nowrap}
.vert b{font-weight:800;color:var(--ink)}
.ring{position:absolute;width:18px;height:18px;border:1.5px solid var(--blue);border-radius:50%}
.ring::after{content:"";position:absolute;left:4px;top:4px;width:7px;height:7px;border-radius:50%;background:var(--blue)}
.ring.cyan{border-color:var(--cyan)} .ring.cyan::after{background:var(--cyan)}
.h-sm{font-weight:700;font-size:11px;line-height:1.15}
.h-up{font-weight:700;font-size:11px;text-transform:uppercase;line-height:1.2}
.body{font-size:6.5px;line-height:1.45;color:var(--muted)}
.body.light{color:rgba(255,255,255,.85)}
.label{font-size:6px;font-weight:600;letter-spacing:.05em;color:var(--ink);display:flex;align-items:center;gap:6px;white-space:nowrap}
.label::before{content:"";width:5px;height:5px;background:var(--ink)}
.rule{position:absolute;height:1px;background:var(--rule)}
.greybar{position:absolute;height:9px;background:var(--bar)}
.footer{position:absolute;font-size:5px;letter-spacing:.05em;color:var(--muted);white-space:nowrap}
.footer.accent{color:#9fb6e3}
.num{position:absolute;width:67px;height:67px;border:2px solid var(--blue);border-radius:50%;display:flex;align-items:center;justify-content:center;font-weight:800;font-size:26px;color:var(--blue)}
.num.cyan{border-color:var(--cyan);color:var(--cyan)}
.panel{position:absolute;color:#fff;padding:18px 16px}
.icon{position:absolute;width:30px;height:30px;border:1.5px solid var(--cyan);border-radius:50%}
.icon svg{position:absolute;left:6px;top:6px}
</style>
</head>
<body>

<!-- Cover -->
<section class="page cover" style="left:376px;top:121px;width:448px;height:633px">
  <div class="abs brand-mark" style="left:56px;top:54px;font-size:20px"><i></i>PEAK BY FORM</div>
  <div class="abs" style="left:246px;top:42px;width:147px;height:66px">
    <div style="height:1px;background:var(--rule);margin-bottom:3px"></div>
    <div style="height:1px;background:var(--rule);margin-bottom:3px"></div>
    <div style="height:1px;background:var(--rule);margin-bottom:3px"></div>
    <div class="brand" style="margin-top:16px;font-size:11px">PEAK BY FORM</div>
    <div style="height:1px;background:var(--rule);margin-top:14px"></div>
  </div>
  <div class="photo ph-sky" role="img" aria-label="Evening view of a mixed-use building with a lit fitness centre" style="left:0;top:158px;width:221px;height:475px"></div>
  <div class="photo ph-sky" role="img" aria-label="Lower part of the building with a blue-tinted glass fitness centre" style="left:0;top:365px;width:393px;height:268px;background:linear-gradient(180deg,#4e3a30 0%,#5a4d48 40%,#2f66cc 75%,#2b5fbf 100%)"></div>
  <h1 class="abs" style="left:246px;top:160px;font-size:16px;font-weight:800;line-height:1.15">STATEMENT OF<br>QUALIFICATION</h1>
  <div class="ring" style="left:246px;top:230px"></div>
  <div class="abs" style="left:272px;top:232px;font-size:9px;font-weight:600">DALE MARSH</div>
  <p class="abs body" style="left:246px;top:266px;width:140px">Maio magnitate pa dolorat id quatio. Agnam velest et aut aliquodit volore consequi dessitatur sus. Nestionem quuntor sunto mo corercis consequie asini nostiberem quiderum fuga.</p>
  <div class="abs" style="left:246px;top:357px;width:147px;height:6px;background:var(--blue)"></div>
  <div class="abs" style="left:393px;top:591px;width:55px;height:1px;background:var(--rule)"></div>
  <div class="abs" style="left:326px;top:588px;font-size:4.5px;color:#fff">PEAKBYFORM.CO</div>
</section>

<!-- Spread: consultant / values -->
<section class="page spread" style="left:150px;top:899px;width:898px;height:633px">
  <div class="abs brand-mark" style="left:38px;top:42px;font-size:11px"><i></i>PEAK BY FORM</div>
  <div class="rule" style="left:260px;top:53px;width:320px"></div>
  <div class="abs label" style="left:495px;top:38px">OUR VALUES</div>

  <div class="sq blue" style="left:34px;top:95px"></div>
  <div class="vert" style="left:34px;bottom:296px">WELCOME TO<br><b>CONSULTANT</b></div>
  <div class="photo ph-sky" role="img" aria-label="Dusk view of a modern apartment building" style="left:97px;top:95px;width:352px;height:245px;background:linear-gradient(180deg,#6b8fbb 0%,#b6a89a 40%,#5c4438 70%,#4c4a52 100%)"></div>
  <div class="abs" style="left:97px;top:340px;width:352px;height:14px;background:var(--blue)"></div>
  <div class="photo ph-portrait" role="img" aria-label="Portrait of the consultant" style="left:33px;top:388px;width:157px;height:136px"></div>
  <div class="rule" style="left:33px;top:558px;width:160px"></div>
  <div class="ring" style="left:232px;top:397px"></div>
  <h2 class="abs" style="left:232px;top:425px;font-size:18px;font-weight:800">CONSULTANT</h2>
  <p class="abs" style="left:232px;top:470px;font-size:10px;line-height:1.3;color:#444">Maio magnitate pa<br>dolorat id quatio.</p>
  <p class="abs body" style="left:232px;top:510px;width:150px">Maio magnitate pa dolorat id quatio. Agnam velest et aut aliquodit volore consequi dessitatur sus. Nestionem quuntor sunto mo corercis consequie asini nostiberem quiderum fuga.</p>

  <div class="sq cyan" style="left:495px;top:97px"></div>
  <div class="vert" style="left:502px;bottom:296px"><b>OUR VALUES</b></div>
  <div class="photo ph-sky-sm" role="img" aria-label="Narrow view of the building facade" style="left:452px;top:358px;width:67px;height:220px"></div>
  <div class="photo ph-sky-sm" role="img" aria-label="Building facade at sunset" style="left:721px;top:0;width:177px;height:226px"></div>
  <div class="ring cyan" style="left:554px;top:98px"></div>
  <div class="abs h-sm" style="left:584px;top:97px">Maio magnitate pa<br>dolorat id quatio.</div>
  <div class="abs" style="left:554px;top:138px;width:167px;height:88px;background:var(--cyan);padding:10px 14px">
    <p class="body light">Maio magnitate pa dolorat id quatio. Agnam velest et aut aut aliquodit.</p>
    <p class="body light" style="margin-top:5px">Maio magnitate pa dolorat id quatio. Agnam velest et aut aut aliquodit.</p>
  </div>

  <div class="icon" style="left:557px;top:250px"><svg width="16" height="16" viewBox="0 0 16 16" fill="none" stroke="#0db3d6" stroke-width="1.4"><path d="M2 14V9M6 14V6M10 14V8M14 14V3"/></svg></div>
  <div class="abs h-sm" style="left:557px;top:292px">Maio magnitate pa<br>dolorat id quatio.</div>
  <p class="abs body" style="left:557px;top:322px;width:140px">Maio magnitate pa dolorat id quatio. Agnam velest et aut aliquodit volore consequi dessitatur sus. Nestionem quuntor sunto mo corercis consequie asini nostiberem quiderum fuga.</p>
  <div class="icon" style="left:722px;top:250px"><svg width="16" height="16" viewBox="0 0 16 16" fill="none" stroke="#0db3d6" stroke-width="1.4"><path d="M2 8l3-3 3 3 3-3 3 3M4 10l3 3 5-5"/></svg></div>
  <div class="abs h-sm" style="left:722px;top:292px">Maio magnitate pa<br>dolorat id quatio.</div>
  <p class="abs body" style="left:722px;top:322px;width:140px">Maio magnitate pa dolorat id quatio. Agnam velest et aut aliquodit volore consequi dessitatur sus. Nestionem quuntor sunto mo corercis consequie asini nostiberem quiderum fuga.</p>
  <div class="rule" style="left:557px;top:388px;width:130px"></div>
  <div class="rule" style="left:722px;top:388px;width:130px"></div>
  <div class="icon" style="left:557px;top:410px"><svg width="16" height="16" viewBox="0 0 16 16" fill="none" stroke="#0db3d6" stroke-width="1.4"><path d="M3 2v12M6 2v12M10 2v12M13 2v12M1 6h4M8 10h4"/></svg></div>
  <div class="abs h-sm" style="left:557px;top:450px">Maio magnitate pa<br>dolorat id quatio.</div>
  <p class="abs body" style="left:557px;top:480px;width:140px">Maio magnitate pa dolorat id quatio. Agnam velest et aut aliquodit volore consequi dessitatur sus. Nestionem quuntor sunto mo corercis consequie asini nostiberem quiderum fuga.</p>
  <div class="icon" style="left:722px;top:410px"><svg width="16" height="16" viewBox="0 0 16 16" fill="none" stroke="#0db3d6" stroke-width="1.4"><circle cx="8" cy="8" r="6"/><path d="M8 8V2M8 8l4 4"/></svg></div>
  <div class="abs h-sm" style="left:722px;top:450px">Maio magnitate pa<br>dolorat id quatio.</div>
  <p class="abs body" style="left:722px;top:480px;width:140px">Maio magnitate pa dolorat id quatio. Agnam velest et aut aliquodit volore consequi dessitatur sus. Nestionem quuntor sunto mo corercis consequie asini nostiberem quiderum fuga.</p>
  <div class="greybar" style="left:557px;top:565px;width:341px"></div>

  <div class="footer" style="left:28px;top:610px">2</div>
  <div class="footer accent" style="left:104px;top:610px">PEAK BY FORM</div>
  <div class="footer" style="left:330px;top:610px">PEAKBYFORM.CO</div>
  <div class="footer" style="left:556px;top:610px">PEAKBYFORM.CO</div>
  <div class="footer accent" style="left:735px;top:610px">PEAK BY FORM</div>
  <div class="abs" style="left:834px;top:600px;width:1px;height:33px;background:var(--rule)"></div>
  <div class="footer" style="left:865px;top:610px">3</div>
</section>

<!-- Spread: buyers agent -->
<section class="page spread" style="left:157px;top:1678px;width:891px;height:631px">
  <div class="abs brand-mark" style="left:38px;top:44px;font-size:11px"><i></i>PEAK BY FORM</div>
  <div class="sq cyan" style="left:35px;top:91px"></div>
  <div class="vert" style="left:32px;bottom:347px">WHY YOU NEED<br>A BUYERS <b>AGENT</b></div>
  <div class="ring cyan" style="left:105px;top:95px"></div>
  <div class="abs h-up" style="left:103px;top:161px">Maio magnitate pa<br>dolorat id quatio.</div>
  <p class="abs body" style="left:103px;top:193px;width:140px">Maio magnitate pa dolorat id quatio. Agnam velest et aut aliquodit volore consequi dessitatur sus. Nestionem quuntor sunto mo corercis consequie asini nostiberem quiderum fuga.</p>
  <div class="photo ph-gym" role="img" aria-label="Row of cardio machines in a bright gym" style="left:269px;top:0;width:175px;height:262px"></div>
  <div class="rule" style="left:32px;top:291px;width:827px"></div>
  <div class="num cyan" style="left:28px;top:381px">1</div>
  <div class="num cyan" style="left:28px;top:461px">2</div>
  <div class="panel" role="img" aria-label="Cyan-tinted photo of treadmills by large windows" style="left:104px;top:317px;width:341px;height:233px;background:linear-gradient(90deg,#0db3d6 0%,#0db3d6 45%,#3f8fa8 75%,#5b6e78 100%)">
    <div class="h-up" style="font-size:13px">Maio magnitate pa<br>dolorat id quatio.</div>
    <div class="h-sm" style="margin-top:14px">Maio magnitate pa<br>dolorat id quatio.</div>
    <p class="body light" style="width:150px">Maio magnitate pa dolorat id quatio. Agnam velest et aut aliquodit volore sus.</p>
    <div class="h-sm" style="margin-top:14px">Maio magnitate pa<br>dolorat id quatio.</div>
    <p class="body light" style="width:150px">Maio magnitate pa dolorat id quatio. Agnam velest et aut aliquodit volore sus.</p>
  </div>
  <div class="greybar" style="left:104px;top:565px;width:341px"></div>

  <div class="abs label" style="left:493px;top:40px">WHAT DOES A BUYERS AGENT DO</div>
  <div class="sq blue" style="left:491px;top:91px"></div>
  <div class="vert" style="left:488px;bottom:347px">WHAT DOES A<br>BUYERS <b>AGENT DO</b></div>
  <div class="ring" style="left:571px;top:95px"></div>
  <div class="abs h-up" style="left:562px;top:161px">Maio magnitate pa<br>dolorat id quatio.</div>
  <p class="abs body" style="left:562px;top:193px;width:140px">Maio magnitate pa dolorat id quatio. Agnam velest et aut aliquodit volore consequi dessitatur sus. Nestionem quuntor sunto mo corercis consequie asini nostiberem quiderum fuga.</p>
  <div class="photo ph-gym-dark" role="img" aria-label="Strength equipment on a wooden gym floor" style="left:712px;top:0;width:179px;height:262px"></div>
  <div class="num" style="left:484px;top:381px">1</div>
  <div class="num" style="left:484px;top:461px">2</div>
  <div class="panel" role="img" aria-label="Blue-tinted photo of a weight room" style="left:563px;top:317px;width:328px;height:233px;background:linear-gradient(90deg,#3d6fcf 0%,#3d6fcf 45%,#4f78bf 75%,#6a7a95 100%)">
    <div class="h-up" style="font-size:13px">Maio magnitate pa<br>dolorat id quatio.</div>
    <div class="h-sm" style="margin-top:14px">Maio magnitate pa<br>dolorat id quatio.</div>
    <p class="body light" style="width:150px">Maio magnitate pa dolorat id quatio. Agnam velest et aut aliquodit volore sus.</p>
    <div class="h-sm" style="margin-top:14px">Maio magnitate pa<br>dolorat id quatio.</div>
    <p class="body light" style="width:150px">Maio magnitate pa dolorat id quatio. Agnam velest et aut aliquodit volore sus.</p>
  </div>
  <div class="greybar" style="left:563px;top:565px;width:328px"></div>

  <div class="footer" style="left:28px;top:606px">4</div>
  <div class="footer accent" style="left:104px;top:606px">PEAK BY FORM</div>
  <div class="footer" style="left:326px;top:606px">PEAKBYFORM.CO</div>
  <div class="footer" style="left:488px;top:606px">PEAKBYFORM.CO</div>
  <div class="footer accent" style="left:728px;top:606px">PEAK BY FORM</div>
  <div class="abs" style="left:828px;top:596px;width:1px;height:35px;background:var(--rule)"></div>
  <div class="footer" style="left:860px;top:606px">5</div>
</section>

<!-- Spread: process -->
<section class="page spread" style="left:157px;top:2455px;width:894px;height:631px">
  <div class="abs brand-mark" style="left:38px;top:44px;font-size:11px"><i></i>PEAK BY FORM</div>
  <div class="sq cyan" style="left:36px;top:92px;width:25px;height:25px"></div>
  <div class="vert" style="left:38px;bottom:366px"><b>THE PROCESS</b></div>
  <div class="photo" role="img" aria-label="Overhead view of a gym floor with equipment" style="left:83px;top:91px;width:290px;height:174px;background:linear-gradient(180deg,#6f7074 0%,#8a8b8f 50%,#4d4e52 100%)"></div>
  <div class="photo ph-gym-red" role="img" aria-label="Weight room with racks and red flooring" style="left:393px;top:0;width:501px;height:265px"></div>
  <div class="rule" style="left:32px;top:284px;width:862px"></div>
  <div class="ring cyan" style="left:39px;top:306px"></div>
  <div class="abs" style="left:81px;top:308px;font-size:10px;font-weight:400">MAIO MAGNITATE PA DOLORAT ID QUATIO</div>

  <div class="abs" style="left:38px;top:330px;width:335px;height:230px">
    <div class="abs" style="left:0;top:0;width:158px;height:108px;border:1px solid var(--cyan)"></div>
    <div class="abs" style="left:172px;top:0;width:163px;height:108px;border:1px solid var(--cyan)"></div>
    <div class="abs" style="left:0;top:122px;width:158px;height:108px;border:1px solid var(--cyan)"></div>
    <div class="abs" style="left:172px;top:122px;width:163px;height:108px;border:1px solid var(--cyan)"></div>
    <p class="abs body" style="left:12px;top:10px;width:134px;text-align:center">Maio magnitate pa dolorat id quatio. Agnam velest et aut aliquodit volore consequi dessitatur sus fuga.</p>
    <p class="abs body" style="left:186px;top:10px;width:134px;text-align:center">Maio magnitate pa dolorat id quatio. Agnam velest et aut aliquodit volore consequi dessitatur sus fuga.</p>
    <p class="abs body" style="left:12px;top:176px;width:134px;text-align:center">Maio magnitate pa dolorat id quatio. Agnam velest et aut aliquodit volore consequi dessitatur sus fuga.</p>
    <p class="abs body" style="left:186px;top:176px;width:134px;text-align:center">Maio magnitate pa dolorat id quatio. Agnam velest et aut aliquodit volore consequi dessitatur sus fuga.</p>
    <div class="abs" style="left:0;top:72px;width:158px;height:30px;background:var(--cyan)"></div>
    <div class="abs" style="left:172px;top:72px;width:163px;height:30px;background:var(--cyan)"></div>
    <div class="abs" style="left:0;top:128px;width:158px;height:30px;background:var(--cyan)"></div>
    <div class="abs" style="left:172px;top:128px;width:163px;height:30px;background:var(--cyan)"></div>
    <div class="abs" style="left:30px;top:80px;font-size:5px;font-weight:700;line-height:1.2;text-align:center;width:70px">Maio magnitate pa dolorat id quatio</div>
    <div class="abs" style="left:215px;top:80px;font-size:5px;font-weight:700;line-height:1.2;text-align:center;width:70px">Maio magnitate pa dolorat id quatio</div>
    <div class="abs" style="left:30px;top:136px;font-size:5px;font-weight:700;line-height:1.2;text-align:center;width:70px">Maio magnitate pa dolorat id quatio</div>
    <div class="abs" style="left:215px;top:136px;font-size:5px;font-weight:700;line-height:1.2;text-align:center;width:70px">Maio magnitate pa dolorat id quatio</div>
    <div class="abs" style="left:118px;top:82px;width:28px;height:28px;border-radius:50%;background:#fff;border:1px solid var(--cyan)"></div>
    <div class="abs" style="left:186px;top:82px;width:28px;height:28px;border-radius:50%;background:#fff;border:1px solid var(--cyan)"></div>
    <div class="abs" style="left:118px;top:120px;width:28px;height:28px;border-radius:50%;background:#fff;border:1px solid var(--cyan)"></div>
    <div class="abs" style="left:186px;top:120px;width:28px;height:28px;border-radius:50%;background:#fff;border:1px solid var(--cyan)"></div>
    <div class="abs" style="left:144px;top:92px;width:48px;height:48px;border-radius:50%;background:var(--cyan);border:3px solid #fff"></div>
  </div>

  <div class="ring" style="left:492px;top:345px"></div>
  <div class="abs" style="left:520px;top:348px;font-size:10px">ABOUT MAIO MAGNITAT</div>
  <div class="abs" style="left:446px;top:540px;width:420px;height:30px;background:var(--blue)"></div>
  <div class="abs" style="left:446px;top:369px;width:270px;height:204px;background:var(--blue);padding:18px 44px;color:#fff">
    <div style="font-size:11px;line-height:1.25">Maio magnitate pa<br>dolorat id quatio.</div>
    <p class="body light" style="margin-top:10px">Maio magnitate pa dolorat id quatio. Agnam velest et aut aliquodit volore consequi dessitatur sus. Nestionem quuntor sunto mo corercis consequie asini nostiberem quiderum fuga.</p>
    <p class="body light" style="margin-top:8px">Maio magnitate pa dolorat id quatio. Agnam velest et aut aliquodit volore consequi dessitatur sus. Nestionem quuntor sunto mo corercis consequie asini nostiberem quiderum fuga.</p>
  </div>
  <div class="photo ph-gym-dark" role="img" aria-label="Gym corner with squat racks and a wall mural" style="left:716px;top:330px;width:178px;height:197px;background:linear-gradient(180deg,#2b2c30 0%,#6a6c70 45%,#3e3f44 75%,#8c2a30 100%)"></div>

  <div class="footer" style="left:28px;top:606px">6</div>
  <div class="footer accent" style="left:104px;top:606px">PEAK BY FORM</div>
  <div class="footer" style="left:328px;top:606px">PEAKBYFORM.CO</div>
  <div class="footer" style="left:488px;top:606px">PEAKBYFORM.CO</div>
  <div class="footer accent" style="left:731px;top:606px">PEAK BY FORM</div>
  <div class="abs" style="left:830px;top:596px;width:1px;height:35px;background:var(--rule)"></div>
  <div class="footer" style="left:862px;top:606px">7</div>
</section>

<!-- Back cover -->
<section class="page back" style="left:356px;top:3232px;width:441px;height:625px">
  <div class="abs brand-mark" style="left:69px;top:116px;font-size:12px"><i></i>PEAK BY FORM</div>
  <div class="photo ph-sky" role="img" aria-label="Evening view of a brick apartment building with a blue-lit ground floor" style="left:67px;top:157px;width:374px;height:468px;background:linear-gradient(180deg,#5d84b5 0%,#a9b6c2 25%,#8a6a55 45%,#3d2f2a 70%,#2a5fbf 90%,#1f56b8 100%)"></div>
  <div class="abs" style="left:67px;top:522px;width:295px;height:30px;background:rgba(255,255,255,.25)"></div>
  <div class="abs" style="left:74px;top:508px;font-size:8px;font-weight:700;color:#fff">CONTACT US</div>
  <svg class="abs" style="left:75px;top:531px" width="8" height="11" viewBox="0 0 8 11"><path d="M4 0a4 4 0 0 1 4 4c0 3-4 7-4 7S0 7 0 4a4 4 0 0 1 4-4z" fill="#fff"/><circle cx="4" cy="4" r="1.5" fill="#3d6fcf"/></svg>
  <div class="abs" style="left:88px;top:531px;font-size:5.5px;line-height:1.3;color:#fff">120 Harbor Ave Ste 4, Lakeview,<br>NY 00000</div>
  <svg class="abs" style="left:204px;top:532px" width="9" height="9" viewBox="0 0 10 10"><circle cx="5" cy="5" r="5" fill="#fff"/><path d="M3 2.5l1.2 1.3-.6.8a4 4 0 0 0 1.8 1.8l.8-.6L7.5 7 6.7 8C4.5 8 2 5.5 2 3.3z" fill="#3d6fcf"/></svg>
  <div class="abs" style="left:217px;top:533px;font-size:7px;color:#fff">555-014-2290</div>
  <svg class="abs" style="left:75px;top:564px" width="10" height="7" viewBox="0 0 10 7"><rect width="10" height="7" fill="#fff"/><path d="M0 0l5 4 5-4" stroke="#3d6fcf" fill="none"/></svg>
  <div class="abs" style="left:90px;top:564px;font-size:5.5px;color:#fff">hello@peakbyform.co</div>
</section>

</body>
</html>
```